Bramble Ridge: PowerPoint Design Project

I'm looking for a PowerPoint design that my real estate ompany will use for business proposals and presentations.

Project Deadline Extended
Reason: I'm making the contest "guaranteed payment" as requested by some designers. I'll be using the PowerPoint slides for client presentations. The tag lines given can be a footer or watermark because it just give an idea of what we do and what our company values are.

Target Market(s)

Landlords and corporate companies

Industry/Entity Type

Real Estate

Requirements
Must have
• Company logo
Various Tag lines as a part of the design of the PowerPoint:
1st tagline: We shape your spaces, We grow your neighbourhood
2nd tag line: We focus on steady income, Welcoming every visitor and Caring for each property.
3rd tag line: we are all about people, projects and profits

```html
<!DOCTYPE html>
<html lang="en">
<head>
<meta charset="utf-8">
<title>Bramble Ridge – Presentation Slides</title>
<link href="https://fonts.googleapis.com/css2?family=Open+Sans:wght@400;600;700&family=Arimo:wght@400;700&display=swap" rel="stylesheet">
<style>
  :root{
    --stage:#262626;
    --green:#4cb43f;
    --green-mid:#2e8a22;
    --green-dark:#173f0e;
    --cover-green:#1f6e1b;
    --cover-deep:#0e4d0c;
    --purple:#5b0fb0;
    --ink:#1a1a1a;
    --grey:#6e6e6e;
    --panel:#eef4ec;
  }
  *{box-sizing:border-box;margin:0;padding:0}
  html,body{width:960px;height:1200px;overflow:hidden}
  body{background:radial-gradient(ellipse at center,#343434 0%,var(--stage) 70%);font-family:"Open Sans",sans-serif;position:relative}
  .slide{position:absolute;left:232px;width:497px;height:372px;overflow:hidden}
  .slide--cover{top:18px;background:radial-gradient(circle at 60% 45%,#3a9a30 0%,var(--cover-green) 45%,var(--cover-deep) 100%)}
  .slide--content{background:radial-gradient(ellipse at 45% 40%,#fafafa 0%,#e9e9e9 60%,#d9d9d9 100%)}
  .slide--about{top:406px}
  .slide--chart{top:794px;left:231px;width:498px;height:373px}

  .cover-panel{position:absolute;left:122px;top:0;width:250px;height:372px;background:var(--panel);text-align:center}
  .brand-dot{position:absolute;top:22px;left:114px;width:22px;height:22px;border-radius:50%;background:var(--green)}
  .brand-name{position:absolute;top:58px;left:0;right:0;font-family:"Arimo",sans-serif;font-weight:700;font-size:9.4px;line-height:12px;color:var(--purple)}
  .brand-tag{position:absolute;top:73px;left:0;right:0;font-size:5px;line-height:7px;color:var(--ink);font-weight:600}
  .cover-title{position:absolute;top:146px;left:0;right:0;font-family:"Open Sans",sans-serif;font-weight:700;line-height:1}
  .cover-title .line-big{display:block;color:var(--green);font-size:27px}
  .cover-title .line-mid{display:block;color:var(--purple);font-size:13.5px;margin-top:1px}
  .cover-title .line-row{display:flex;justify-content:center;align-items:center;gap:4px;margin-top:4px}
  .cover-title .line-row .line-big{font-size:29px}
  .cover-title .stack{text-align:left;font-size:9.5px;line-height:1.45}
  .cover-title .stack .w{color:var(--green)}
  .cover-title .stack .t{color:var(--purple)}
  .cover-subtitle{position:absolute;top:240px;left:0;right:0;font-family:"Arimo",sans-serif;font-weight:700;font-size:10px;color:var(--purple)}

  .slide-title{position:absolute;left:33px;top:25px;font-family:"Arimo",sans-serif;font-weight:700;font-size:19.5px;color:var(--green)}
  .title-rule{position:absolute;left:33px;top:55px;width:445px;height:1px;background:#fff;box-shadow:0 3px 8px rgba(0,0,0,.18)}
  .body-copy{position:absolute;left:33px;top:92px;width:436px;font-size:7.1px;line-height:11.2px;color:var(--ink)}
  .bullets{position:absolute;left:100px;top:151px;list-style:none}
  .bullets li{display:flex;align-items:center;height:16.7px;font-size:5.7px;color:var(--green)}
  .bullets svg{width:9px;height:6px;margin-right:15px}

  .footer-line{position:absolute;left:0;right:0;top:349px;height:2px;background:var(--green)}
  .footer-brand{position:absolute;left:29px;top:326px;display:flex;align-items:center;gap:4px;white-space:nowrap}
  .footer-brand .dot{width:14px;height:14px;border-radius:50%;background:var(--green)}
  .footer-brand .name{font-size:6px;font-weight:700;color:var(--green)}
  .footer-tagline{font-size:8.4px;color:var(--grey);margin-left:6px}
  .footer-bar{position:absolute;left:0;right:0;top:351px;height:21px;background:#e4e4e4;font-size:6.3px}
  .footer-bar .project{position:absolute;left:29px;top:6px;color:var(--green);font-weight:600}
  .footer-bar .date{position:absolute;right:36px;top:6px;color:var(--ink)}
  .footer-bar .date b{color:var(--green);font-weight:600}
  .swoosh{position:absolute;left:0;top:0;width:100%;height:100%}
  .page-no{position:absolute;top:326px;font-family:"Arimo",sans-serif;font-weight:700;font-size:24px;line-height:24px;color:#a9a9a9}
  .chart-art{position:absolute;left:0;top:0;width:498px;height:373px;font-family:"Arimo",sans-serif}
</style>
</head>
<body>

<section class="slide slide--cover">
  <div class="cover-panel">
    <span class="brand-dot"></span>
    <p class="brand-name">Bramble Ridge Property Consultants</p>
    <p class="brand-tag">Property Strategy And Leasing Advisors</p>
    <h1 class="cover-title">
      <span class="line-big">SAMPLE TEXT</span>
      <span class="line-mid">FOR LATITUDE TEMPLATE</span>
      <span class="line-row"><span class="line-big">YOU CAN</span><span class="stack"><span class="w">WRITE</span><br><span class="t">TITLE HERE</span></span></span>
    </h1>
    <p class="cover-subtitle">SUBTITLE GOES HERE</p>
  </div>
</section>

<section class="slide slide--content slide--about">
  <h2 class="slide-title">WHAT WE DO?</h2>
  <div class="title-rule"></div>
  <p class="body-copy">Lorem ipsum dolor sit amet, consetetur sadipscing elitr, sed diam nonumy eirmod tempor invidunt ut labore et dolore magna aliquyam erat, sed diam voluptua. At vero eos et accusam et justo duo dolores et ea rebum. Stet clita kasd gubergren, no sea takimata sanctus est Lorem ipsum dolor sit amet. Lorem ipsum dolor sit amet, consetetur sadipscing elit. Stet clita kasd gubergren, no sea takimata sanctus est Lorem ipsum dolor sit amet.</p>
  <ul class="bullets">
    <li><svg viewBox="0 0 9 6"><path d="M0 2h5V0l4 3-4 3V4H0z" fill="#5b0fb0"/></svg>Lorem ipsum dolor sit amet, consetetur sadipscing elitr.</li>
    <li><svg viewBox="0 0 9 6"><path d="M0 2h5V0l4 3-4 3V4H0z" fill="#5b0fb0"/></svg>Sed diam nonumy eirmod tempor invidunt ut labore et dolore.</li>
    <li><svg viewBox="0 0 9 6"><path d="M0 2h5V0l4 3-4 3V4H0z" fill="#5b0fb0"/></svg>Magna aliquyam erat, sed diam voluptua.</li>
    <li><svg viewBox="0 0 9 6"><path d="M0 2h5V0l4 3-4 3V4H0z" fill="#5b0fb0"/></svg>At vero eos et accusam et justo duo dolores et ea rebum.</li>
    <li><svg viewBox="0 0 9 6"><path d="M0 2h5V0l4 3-4 3V4H0z" fill="#5b0fb0"/></svg>Stet clita kasd gubergren, no sea takimata sanctus est.</li>
    <li><svg viewBox="0 0 9 6"><path d="M0 2h5V0l4 3-4 3V4H0z" fill="#5b0fb0"/></svg>Lorem ipsum dolor sit amet. Lorem ipsum dolor sit amet, consetetur sadipscing elit.</li>
  </ul>
  <svg class="swoosh" viewBox="0 0 497 372">
    <path d="M330 349 C400 346 430 338 435 332 L435 341 C420 346 390 348 380 349 Z" fill="#5b0fb0"/>
    <path d="M340 349 C390 347 425 343 435 340 L435 349 Z" fill="#4cb43f"/>
    <path d="M459 318 C475 312 488 306 497 300 L497 307 C488 312 475 318 459 323 Z" fill="#4cb43f"/>
    <path d="M459 323 C475 318 488 312 497 307 L497 316 C488 320 475 325 459 329 Z" fill="#5b0fb0"/>
    <path d="M459 329 C475 325 488 320 497 316 L497 349 L459 349 Z" fill="#4cb43f"/>
  </svg>
  <span class="page-no" style="left:440px">2</span>
  <div class="footer-brand"><span class="dot"></span><span class="name">Bramble Ridge</span><span class="footer-tagline">We shape your spaces,&nbsp; We grow your neighbourhood</span></div>
  <div class="footer-line"></div>
  <div class="footer-bar"><span class="project">Your Project Name Here....</span><span class="date"><b>Date:</b> 03/04/2013</span></div>
</section>

<section class="slide slide--content slide--chart">
  <h2 class="slide-title">CHART</h2>
  <div class="title-rule"></div>
  <svg class="chart-art" viewBox="0 0 498 373" role="img" aria-label="Bar chart of three categories across four diagrams">
    <g font-size="5" font-weight="700" fill="#333">
      <rect x="323" y="68" width="7" height="7" fill="#4cb43f"/><text x="333" y="74">Category 1</text>
      <rect x="363" y="68" width="7" height="7" fill="#2e8a22"/><text x="373" y="74">Category 3</text>
      <rect x="402" y="68" width="7" height="7" fill="#173f0e"/><text x="412" y="74">Category 3</text>
    </g>
    <g stroke="#8a8a8a" stroke-width=".6">
      <line x1="63" y1="258.2" x2="461" y2="258.2"/><line x1="63" y1="241.4" x2="461" y2="241.4"/>
      <line x1="63" y1="224.6" x2="461" y2="224.6"/><line x1="63" y1="207.8" x2="461" y2="207.8"/>
      <line x1="63" y1="191" x2="461" y2="191"/><line x1="63" y1="174.2" x2="461" y2="174.2"/>
      <line x1="63" y1="157.4" x2="461" y2="157.4"/><line x1="63" y1="140.6" x2="461" y2="140.6"/>
      <line x1="63" y1="123.8" x2="461" y2="123.8"/><line x1="63" y1="107" x2="461" y2="107"/>
      <line x1="63" y1="275" x2="461" y2="275" stroke="#555"/><line x1="63" y1="96" x2="63" y2="275" stroke="#555"/>
    </g>
    <g font-size="7" fill="#555" text-anchor="end">
      <text x="50" y="277">0</text><text x="50" y="260">1</text><text x="50" y="243">2</text><text x="50" y="226">3</text>
      <text x="50" y="210">4</text><text x="50" y="193">5</text><text x="50" y="176">6</text><text x="50" y="159">7</text>
      <text x="50" y="142">8</text><text x="50" y="126">9</text><text x="50" y="109">10</text>
    </g>
    <g>
      <rect x="101" y="223" width="14.5" height="52" fill="#4cb43f"/>
      <rect x="115.5" y="134" width="14.5" height="141" fill="#2e8a22"/>
      <rect x="130" y="198" width="14.5" height="77" fill="#173f0e"/>
      <rect x="195" y="179" width="14.5" height="96" fill="#4cb43f"/>
      <rect x="209.5" y="198" width="14.5" height="77" fill="#2e8a22"/>
      <rect x="224" y="236" width="14.5" height="39" fill="#173f0e"/>
      <rect x="292" y="216" width="14.5" height="59" fill="#4cb43f"/>
      <rect x="306.5" y="198" width="14.5" height="77" fill="#2e8a22"/>
      <rect x="321" y="159" width="14.5" height="116" fill="#173f0e"/>
      <rect x="383" y="139" width="14.5" height="136" fill="#4cb43f"/>
      <rect x="397.5" y="179" width="14.5" height="96" fill="#2e8a22"/>
      <rect x="412" y="198" width="14.5" height="77" fill="#173f0e"/>
    </g>
    <g font-size="6.5" font-weight="700" fill="#444" text-anchor="middle">
      <text x="123" y="293">Diagram 1</text><text x="217" y="293">Diagram 2</text>
      <text x="314" y="293">Diagram 3</text><text x="405" y="293">Diagram 4</text>
    </g>
    <path d="M330 350 C400 347 430 339 435 333 L435 342 C420 347 390 349 380 350 Z" fill="#5b0fb0"/>
    <path d="M340 350 C390 348 425 344 435 341 L435 350 Z" fill="#4cb43f"/>
    <path d="M459 319 C475 313 488 307 498 301 L498 308 C488 313 475 319 459 324 Z" fill="#4cb43f"/>
    <path d="M459 324 C475 319 488 313 498 308 L498 317 C488 321 475 326 459 330 Z" fill="#5b0fb0"/>
    <path d="M459 330 C475 326 488 321 498 317 L498 350 L459 350 Z" fill="#4cb43f"/>
  </svg>
  <span class="page-no" style="left:435px">10</span>
  <div class="footer-brand"><span class="dot"></span><span class="name">Bramble Ridge</span><span class="footer-tagline" style="font-size:7.2px">We focus on steady income, Welcoming every visitor and Caring for each property.</span></div>
  <div class="footer-line"></div>
  <div class="footer-bar"><span class="project">Your Project Name Here....</span><span class="date"><b>Date:</b> 03/04/2013</span></div>
</section>

</body>
</html>
```